Wordpress Website for electrician

I'm looking for an easy to maintain website for my electrical contracting business. Need a professional and appealing site.
Im wanting a website where clients can come on and look at services we offer, case studies and advertise our services.
Colours I'm wanting to incorporate are green, white, black and grey
I'm wanting a big slide show on main page where I can place advertising etc.
Menu is to include home, services, our work, specials, energy efficiency and contact
My existing site is www.trelwirefix.com.au
Updates
looking for something with a similar layout to this website
Target Market(s)
Businesses
Industry/Entity Type
Electrician
Look and feel

```html
<!DOCTYPE html>
<html lang="en">
<head>
<meta charset="utf-8">
<title>trelwirefix – electrical contractor</title>
<link rel="stylesheet" href="https://fonts.googleapis.com/css2?family=Arimo:wght@400;700&family=Open+Sans:wght@600;700&display=swap">
<style>
  :root {
    --green: #3aaa35;
    --green-light: #9cc83c;
    --black: #111111;
    --ink: #222222;
    --grey-text: #555555;
    --rule: #c8c8c8;
    --footer-bg: #e2e2e2;
    --orange: #f7a000;
    --white: #ffffff;
  }
  * { box-sizing: border-box; margin: 0; padding: 0; }
  html, body { width: 1200px; height: 1005px; overflow: hidden; background: var(--white); }
  body { position: relative; font-family: "Arimo", Arial, sans-serif; color: var(--ink); }
  .top-bar { position: absolute; left: 0; top: 0; width: 1200px; height: 11px; background: var(--black); }

  .brand { position: absolute; left: 240px; top: 40px; display: flex; align-items: center; gap: 8px; }
  .brand-dot { width: 26px; height: 26px; border-radius: 50%; background: var(--green); }
  .brand-name { font-size: 26px; font-weight: 700; color: var(--green); letter-spacing: -0.5px; }
  .brand-tag { position: absolute; left: 274px; top: 72px; font-size: 9px; color: #888; }

  .main-nav { position: absolute; right: 240px; top: 60px; display: flex; gap: 30px; }
  .main-nav a { font-size: 10px; font-weight: 700; color: var(--green); text-decoration: none; }
  .main-nav a.current { color: var(--black); }

  .rule { position: absolute; left: 240px; width: 720px; height: 1px; background: var(--rule); }

  .hero-title { position: absolute; left: 262px; top: 156px; font-family: "Open Sans", sans-serif; font-weight: 700; font-size: 59px; line-height: 56px; letter-spacing: -1px; }
  .hero-title .green { color: var(--green); display: block; }
  .hero-title .dark { color: var(--black); display: block; text-shadow: 2px 2px 2px rgba(0,0,0,.25); }
  .promo-bar { position: absolute; left: 266px; top: 348px; width: 332px; height: 34px; background: var(--black); display: flex; justify-content: space-between; align-items: center; padding: 0 8px 0 10px; font-size: 12px; font-weight: 700; }
  .promo-bar .label { color: #bbb; }
  .promo-bar .cta { color: var(--orange); }
  .grass { position: absolute; left: 240px; top: 383px; width: 350px; height: 32px; background: linear-gradient(#7bbd3a, #3f8a1f); }
  .tree { position: absolute; left: 653px; top: 128px; width: 234px; height: 287px; background: radial-gradient(ellipse at 50% 35%, #a7cf4a 0%, #8cc540 45%, #cfe3a0 80%, #ffffff 100%); border-radius: 45% 45% 10% 10%; }

  .section-head { position: absolute; font-size: 14px; font-weight: 700; color: var(--black); padding-bottom: 8px; }
  .section-head::before { content: "→"; font-weight: 400; margin-right: 12px; }
  .column-head { width: 212px; border-bottom: 4px solid var(--black); }
  .small-head { font-size: 10px; }

  .column { position: absolute; top: 485px; width: 212px; font-size: 9.5px; line-height: 15px; color: var(--grey-text); }
  .news-item { margin-bottom: 15px; }
  .read-more { font-size: 9.5px; font-weight: 700; color: var(--orange); margin-top: 17px; }
  .read-more::before { content: "→"; color: var(--black); margin-right: 12px; font-weight: 400; }
  .benefit { display: flex; gap: 10px; line-height: 11px; margin-bottom: 11px; }
  .tick { flex: 0 0 11px; height: 11px; background: #ccc; margin-top: 1px; }
  .quote-by { font-style: italic; color: var(--ink); margin-top: 14px; }

  .portfolio-item { position: absolute; top: 674px; width: 162px; height: 101px; }
  .portfolio-item .view { position: absolute; right: 0; bottom: 0; width: 46px; height: 15px; background: var(--orange); font-size: 9px; font-weight: 700; color: var(--black); text-align: center; line-height: 15px; }

  .blog-text { position: absolute; left: 240px; top: 853px; width: 500px; font-size: 9.5px; line-height: 15px; color: var(--grey-text); }
  .social { position: absolute; left: 795px; top: 851px; display: flex; gap: 10px; }
  .social span { width: 25px; height: 25px; border-radius: 50%; }

  .site-footer { position: absolute; left: 0; top: 928px; width: 1200px; height: 77px; background: var(--footer-bg); }
  .footer-links { position: absolute; left: 241px; top: 23px; font-size: 9.5px; color: #444; word-spacing: 2px; }
  .copyright { position: absolute; left: 241px; top: 39px; font-size: 9.5px; color: #444; }
  .footer-brand { position: absolute; left: 806px; top: 24px; display: flex; align-items: center; gap: 6px; }
  .footer-brand .brand-dot { width: 22px; height: 22px; }
  .footer-brand .brand-name { font-size: 21px; }
</style>
</head>
<body>
  <div class="top-bar"></div>

  <header>
    <div class="brand"><span class="brand-dot"></span><span class="brand-name">trelwirefix</span></div>
    <div class="brand-tag">electrical contractor</div>
    <nav class="main-nav">
      <a class="current">HOME</a><a>OUR WORK</a><a>SERVICES</a><a>SPECIAL</a><a>ENERGY EFFCIENCY</a><a>CONTACT US</a>
    </nav>
  </header>
  <div class="rule" style="top:116px"></div>

  <section class="hero">
    <h1 class="hero-title"><span class="green">BE GREEN</span><span class="dark">SAVE MONEY</span></h1>
    <div class="grass" role="img" aria-label="Strip of green grass"></div>
    <div class="promo-bar"><span class="label">LED IS THE FUTURE</span><span class="cta">VIEW SPECIAL→</span></div>
    <div class="tree" role="img" aria-label="Illustration of a green money tree growing on a globe"></div>
  </section>
  <div class="rule" style="top:430px"></div>

  <section>
    <h2 class="section-head column-head" style="left:240px;top:445px">NEWS</h2>
    <div class="column" style="left:240px">
      <p class="news-item">L24/08/2012: Another ECIA Excellence Award for Halvern Brooks – for the ACT team</p>
      <p class="news-item" style="margin-top:12px">24/08/2012: Another ECIA Excellence Award for Halvern Brooks – for the ACT team</p>
      <p class="read-more">READ</p>
    </div>

    <h2 class="section-head column-head" style="left:494px;top:445px">OUR BENEFITS</h2>
    <div class="column" style="left:494px">
      <div class="benefit"><span class="tick"></span><p>Lorem ipsum dolor sit amet, consectetur adipiscing elit. Pellentesque quis nulla id orci malesuada porta posuere quis massa.</p></div>
      <div class="benefit"><span class="tick"></span><p>Nunc vitae purus non augue scelerisque ultricies vitae et velit. Sed vitae lectus id sem lobortis scelerisque. Praesent eget consequat</p></div>
      <div class="benefit"><span class="tick"></span><p>Lorem ipsum dolor sit amet, consectetur adipiscing elit. Pellentesque quis nulla id orci malesuada porta posuere quis massa.</p></div>
    </div>

    <h2 class="section-head column-head" style="left:748px;top:445px">TESTIMONIALS</h2>
    <div class="column" style="left:748px">
      <p>Lorem ipsum dolor sit amet, consectetur adipiscing elit. Pellentesque quis nulla id orci malesuada porta posuere quis massa. Nunc vitae purus non augue scelerisque ultricies vitae et velit. Sed vitae lectus id sem lobortis scelerisque.</p>
      <p class="quote-by">Mara, Brightlinework.com</p>
    </div>
  </section>
  <div class="rule" style="top:632px"></div>

  <section>
    <h2 class="section-head" style="left:240px;top:646px">OUR PORTFOLIO</h2>
    <div class="portfolio-item" style="left:240px;background:#8a7a6a" role="img" aria-label="Photo of switchboard wiring with orange cables"><span class="view">VIEW →</span></div>
    <div class="portfolio-item" style="left:426px;background:#9a9a98" role="img" aria-label="Photo of an outdoor air conditioning unit by a building"><span class="view">VIEW →</span></div>
    <div class="portfolio-item" style="left:612px;background:#a0604a" role="img" aria-label="Photo of a split system unit on a brick wall"><span class="view">VIEW →</span></div>
    <div class="portfolio-item" style="left:798px;background:#5a5550" role="img" aria-label="Photo of an air conditioning unit on a roof"><span class="view"></span></div>
  </section>
  <div class="rule" style="top:805px"></div>

  <section>
    <h2 class="section-head small-head" style="left:240px;top:823px">BLOG UPDATES</h2>
    <p class="blog-text">Lorem ipsum dolor sit amet, consectetur adipiscing elit. Pellentesque quis nulla id orci malesuada porta posuere quis massa. Nunc vitae purus non augue scelerisque ultricies vitae et velit. Sed vitae lectus id sem lobortis scelerisque. Praesent eget consequat libero.</p>
    <h2 class="section-head small-head" style="left:798px;top:823px">CONECNT WITH US</h2>
    <div class="social">
      <span style="background:#3fb2e6"></span><span style="background:#3b5a99"></span><span style="background:#cfcfcf"></span><span style="background:#f28a1a"></span>
    </div>
  </section>

  <footer class="site-footer">
    <p class="footer-links">Home | About Us | Special | Our Work | Services | Blog | Site Map | Energy efficiancy | Contact Us</p>
    <p class="copyright">© 2013 All Rights Reserved</p>
    <div class="footer-brand"><span class="brand-dot"></span><span class="brand-name">trelwirefix</span></div>
  </footer>
</body>
</html>
```